Classic and neutral book cover design

We are looking for a classic and neutral book cover design to be used as the template for a series of books to be published. We are hence looking for a template that will allow us to easily change the title name for all books in this series.
The use of very few colours (black and white is welcome) and few design elements is a big bonus. As a source of inspiration we would like to ask you to view the very simple and
If you think you have a cool idea that can add a twist to the formal classic look don't hesitate. Go for it !
Work will be done for a 30 year old Sweden based cultural non-profit called VĂ©lra (www.velrafoundation.example). We work with the publishing and supporting of post-modern art and literature addressing contemporary topics but are also involved in assisting projects of cultural preservation.
Target Market(s)
The audience is expected to have some form of interest in culture but could range from hobbyist readers to tenure track scholars
Industry/Entity Type
Non-Profit
Requirements
Must have
- General:
- Classic and neutral feel
- Preferably very simple and few shapes
- usage of few colours (black and white is welcome)
Information to be displayed on the cover is:
- Author
- Title
- type of work e.g. play/novel (optional)
- publishing house (in this case "Velra Publishing")
Nice to have
- ideas to prevent it from become boring are of course welcome
Should not have
- - too many colours

```html
<!DOCTYPE html>
<html lang="en">
<head>
<meta charset="utf-8">
<title>Book Cover Template</title>
<link rel="stylesheet" href="https://fonts.googleapis.com/css2?family=Antonio:wght@200;400&display=swap">
<style>
  :root {
    --cover-blush: #fce8e2;
    --border-tone: #efd6cf;
    --ink: #0b0b0b;
  }
  html, body {
    margin: 0;
    padding: 0;
    overflow: hidden;
    background: var(--cover-blush);
  }
  .cover {
    position: relative;
    width: 751px;
    height: 1200px;
    background: var(--cover-blush);
    overflow: hidden;
  }
  .cover-border {
    position: absolute;
    inset: 0;
    width: 751px;
    height: 1200px;
  }
  .author-name {
    position: absolute;
    top: 186px;
    left: 0;
    width: 751px;
    margin: 0;
    text-align: center;
    font-family: "Antonio", sans-serif;
    font-weight: 200;
    font-size: 50px;
    line-height: 1;
    letter-spacing: 0.14em;
    color: var(--ink);
  }
  .book-title {
    position: absolute;
    top: 268px;
    left: 26px;
    width: 751px;
    margin: 0;
    text-align: center;
    font-family: "Antonio", sans-serif;
    font-weight: 400;
    font-size: 158px;
    line-height: 1;
    letter-spacing: 0.06em;
    color: var(--ink);
  }
</style>
</head>
<body>
  <main class="cover">
    <svg class="cover-border" viewBox="0 0 751 1200" role="img" aria-label="Ornamental lattice border framing the cover">
      <path fill="var(--border-tone)" fill-rule="evenodd"
            d="M13 0 H738 V1200 H13 Z M83 67 H667 V1131 H83 Z"/>
    </svg>
    <p class="author-name">AUTOR NAME</p>
    <h1 class="book-title">TITLE</h1>
  </main>
</body>
</html>
```